Clean, Corporate redesign of existing website

We require a clean corporate professional redesign of our existing poor website, although a simple and elegant structure is required we would like the designer to concentrate on the little things and finishes to give the site a highly professional feel.
The company have supplied the following websites as to use as inspiration http://www.tollardminerals.com/ they like the clean, professional feel of the website
and the fact that the website captures the feel of their industry. Another clean and professional site they liked the look of was http://www.brindlefishbites.co.uk/ .
Another inspirational (page level only) http://www.harrowgateexpohall.com/thefacilities/floor-maps-and-specifications/ we like the top image and the corporate feel the images give. Auto cad drawings as images or a search for electrical services will fetch up a good selection of images to use as placeholders
A full brief, logos, images etc have been supplied
update: the sector is industrial electrical services, so more towards factory switches and equipement, not domestic light-bulbs etc this is important when choosing images for the site.
Updates
Thank you all for your designs, i will be presenting the best to the company tomorrow who will pick the design that suits so please get any remaining designs to me by tomorrow morning (GMT time) at the latest to be included in the presentation.
Target Market(s)
Business owners and CEO'S
Industry/Entity Type
Electrical
Look and feel

```html
<!DOCTYPE html>
<html lang="en">
<head>
<meta charset="utf-8">
<title>Fenwold Electrical Services Limited</title>
<link rel="stylesheet" href="https://fonts.googleapis.com/css2?family=Roboto+Condensed:wght@700&family=Arimo:wght@400&display=swap">
<style>
:root{
  --red:#e2231a;
  --ink:#1a1a1a;
  --grey:#6b6b6b;
  --page:#ffffff;
  --backdrop:#e9e9e9;
  --frame:#c9c9c9;
  --nav-top:#6a6a6a;
  --nav-bottom:#2b2b2b;
  --dot:#8a8a8a;
}
*{margin:0;padding:0;box-sizing:border-box}
html,body{width:1200px;height:1200px;overflow:hidden}
body{position:relative;background:var(--page);font-family:"Arimo",Arial,sans-serif;color:var(--ink);font-size:12px;line-height:14.5px}
.cond{font-family:"Roboto Condensed","Arial Narrow",sans-serif;font-weight:700}
.abs{position:absolute}

.brand{left:150px;top:36px;display:flex;align-items:center;gap:10px;color:var(--ink);font-family:"Roboto Condensed",sans-serif;font-weight:700;font-size:22px;line-height:1}
.brand .mark{width:14px;height:14px;background:var(--red)}

.social{top:46px;left:945px;display:flex;gap:15px}
.social span{display:block;width:20px;height:20px;background:var(--red);border-radius:2px}

.nav{left:130px;top:90px;width:940px;height:34px;background:linear-gradient(var(--nav-top),var(--nav-bottom) 55%,#4a4a4a);display:flex;align-items:center;padding-left:28px;gap:33px}
.nav a{color:#fff;text-decoration:none;font-size:13px;text-transform:uppercase}

.hero-photo{left:130px;top:140px;width:640px;height:240px;background:radial-gradient(ellipse at 40% 45%,#5a5346 0%,#2a2722 35%,#0c0c10 75%)}
.hero-panel{left:770px;top:140px;width:300px;height:240px;background:linear-gradient(#151515,#050505);color:#fff;padding:24px 30px}
.hero-panel h1{font-size:25px;line-height:29px;font-weight:700}
.hero-panel p{margin-top:14px;font-size:12px;line-height:14.5px;color:#f0f0f0}
.dots{left:885px;top:348px;display:flex;gap:9px}
.dots span{width:11px;height:11px;border-radius:50%;background:var(--dot)}
.dots span:first-child{background:#c8c8c8}

.backdrop{left:0;top:400px;width:1200px;height:800px;background:var(--backdrop);border-top:1px solid #d5d5d5}
.sheet{left:130px;top:420px;width:940px;height:660px;background:#fff;border:1px solid var(--frame);box-shadow:0 1px 3px rgba(0,0,0,.15)}

h2{color:var(--red);font-family:"Roboto Condensed",sans-serif;font-weight:700;font-size:16px;text-transform:uppercase;line-height:18px}
.intro-photo{left:150px;top:470px;width:117px;height:172px;background:linear-gradient(100deg,#3a3a3a 0 12%,#d8d8d8 20%,#b9b9b9 60%,#e1e1e1)}
.intro-text{left:290px;top:468px;width:520px}
.intro-text p+p{margin-top:14.5px}

.news{left:840px;top:468px;width:190px}
.news .date{color:var(--grey)}
.news .item+.item{margin-top:14px}
.more{margin-top:14px;display:flex;align-items:center;gap:8px}

.contact{left:840px;top:648px;width:210px}
.contact p+p{margin-top:14.5px}

.rule{left:150px;width:900px;border-top:1px dotted #555}
.rule.red{border-top:1px dotted var(--red)}

.sector{top:758px;width:210px}
.sector .photo{margin-top:16px;width:210px;height:110px}
.sector p{margin-top:8px}
.learn{margin-top:10px;color:var(--red);font-size:10px;display:flex;align-items:center;gap:8px}

.footer{left:150px;top:1039px;font-size:10px;color:#333}
</style>
</head>
<body>

<div class="abs brand"><span class="mark"></span>Fenwold Electrical Services Limited</div>

<div class="abs social" aria-label="Social links">
  <span></span><span></span><span></span><span></span>
</div>

<nav class="abs nav cond">
  <a href="#">Home</a><a href="#">Services</a><a href="#">Clients</a><a href="#">Responsabilities</a><a href="#">Contact Us</a>
</nav>

<div class="abs hero-photo" role="img" aria-label="Aerial night view of a city lit up with street lights"></div>
<div class="abs hero-panel">
  <h1 class="cond">Fenwold Electrical<br>Services Limited</h1>
  <p>Established in 2005 Fenwold Electrical Services Limited is an independent company that has grown steadily over that period into a respected Commercial and Domestic Electrical installer providing it's services nationwide.</p>
</div>
<div class="abs dots"><span></span><span></span><span></span><span></span></div>

<div class="abs backdrop"></div>
<div class="abs sheet"></div>

<h2 class="abs" style="left:150px;top:436px">Fenwold Electrical Advantages</h2>
<div class="abs intro-photo" role="img" aria-label="Engineer working on an industrial switchgear panel"></div>
<div class="abs intro-text">
  <p>Professional and reliable, the secret of our success has come from recommendations from our customer base.&nbsp; Our staffing levels allow us to be flexible enough to tackle any size of project, contracts often exceeding 100K, yet we are able to complete the more modest budget competitively.&nbsp; All our work is guaranteed and our help line is always available to our clients to satisfy any after contract queries or concerns.</p>
  <p>As a company we strive to meet exceptional standards of workmanship, we are registered with the National Register for Electrical Installation Standards and all our work is certificated accordingly. All our engineers are fully qualified in their relevant fields and all work there is carried out to BS 7671 standards.</p>
  <p>As Health and safety is always such a major factor in the industry, we always ensure that at least one qualified representative is present on each site.&nbsp; We also employ the services of health and safety consultants on a permanent basis.</p>
</div>

<h2 class="abs" style="left:840px;top:436px">Latest News</h2>
<div class="abs news">
  <div class="item"><div class="date">11 October 2012</div><div>Interim Management Statement</div></div>
  <div class="item"><div class="date">22 August 2012</div><div>Half Yearly Results and Market Briefing</div></div>
  <div class="more">More News
    <svg width="13" height="10" viewBox="0 0 13 10"><rect x=".5" y=".5" width="12" height="9" fill="none" stroke="#333"/><path d="M3 5h6M7 3l2 2-2 2" fill="none" stroke="#333"/></svg>
  </div>
</div>

<h2 class="abs" style="left:840px;top:616px">Quick Contact</h2>
<div class="abs contact">
  <p>Unit 4b Harbour Park, Carrow Rd,<br>DN40 2QX</p>
  <p>Tel: 01632 960418</p>
</div>

<div class="abs rule" style="top:740px"></div>

<div class="abs sector" style="left:150px">
  <h2>Food Industry</h2>
  <div class="photo" role="img" aria-label="Lit timber restaurant building at dusk" style="background:linear-gradient(#7d8a99,#5a5446 50%,#b07a3e 75%,#5c6d4a)"></div>
  <p>Lorem ipsum dolor sit amet, consectetur adipiscing elit. Etiam lobortis auctor justo eu semper.</p>
  <div class="learn">LEARN MORE <svg width="5" height="7" viewBox="0 0 5 7"><path d="M1 1l3 2.5L1 6" fill="none" stroke="#e2231a"/></svg></div>
</div>
<div class="abs sector" style="left:380px">
  <h2>Councils</h2>
  <div class="photo" role="img" aria-label="Engineers climbing a steel pylon structure" style="background:linear-gradient(135deg,#b5b5b5,#6d6d6d 50%,#9a9a9a)"></div>
  <p>Lorem ipsum dolor sit amet, consectetur adipiscing elit. Etiam lobortis auctor justo eu semper.</p>
  <div class="learn">LEARN MORE <svg width="5" height="7" viewBox="0 0 5 7"><path d="M1 1l3 2.5L1 6" fill="none" stroke="#e2231a"/></svg></div>
</div>
<div class="abs sector" style="left:610px">
  <h2>Retail Premises</h2>
  <div class="photo" role="img" aria-label="Hand testing terminal blocks with a multimeter" style="background:linear-gradient(120deg,#c9c9c9,#8a8a8a 40%,#b35a3a 65%,#d6d6d6)"></div>
  <p>Lorem ipsum dolor sit amet, consectetur adipiscing elit. Etiam lobortis auctor justo eu semper.</p>
  <div class="learn">LEARN MORE <svg width="5" height="7" viewBox="0 0 5 7"><path d="M1 1l3 2.5L1 6" fill="none" stroke="#e2231a"/></svg></div>
</div>
<div class="abs sector" style="left:840px">
  <h2>Schools&amp; Colleges</h2>
  <div class="photo" role="img" aria-label="Electrician testing wiring with a meter" style="background:linear-gradient(90deg,#3a2a20,#a07a60 40%,#2c4a8a 70%,#d8d0c0)"></div>
  <p>Lorem ipsum dolor sit amet, consectetur adipiscing elit. Etiam lobortis auctor justo eu semper.</p>
  <div class="learn">LEARN MORE <svg width="5" height="7" viewBox="0 0 5 7"><path d="M1 1l3 2.5L1 6" fill="none" stroke="#e2231a"/></svg></div>
</div>

<div class="abs rule red" style="top:1020px"></div>
<div class="abs footer">© 2012 Copyright Fenwold Electrical Services Limited. All rights reserved</div>

</body>
</html>
```